Bluewake Harbor Skipper Services LLC

I'd like business cards with a logo and words to describe my services and qualifications. I want to emphasize the wide variety of services offered and my professional qualifications. Words to include "Bluewake Harbor Skipper Services LLC", "Motor and Sailing Vessel Delivery, Charter, Surveys, Towing and Instruction". Qualifications I would like to include are "Captain Dale Murrow, USCG Master Mariner, 200 ton, Ocean". Include address, phone and email: "48215 Willowmere Lane, Fairfax Station, VA 22871, (C) 703-555-0187, BluewakeHarborSkipper@mailbay-example.com"

Target Market(s)

I am targeting recreational boaters and commercial customers that need people to operate their boats for charter or delivery to another location.

Industry/Entity Type

boat selling/buying, boat charter, boat recreation

Logo Text

"Motor and Sailing Vessel Delivery, Charters, Surveys, Towing and Instruction"

Requirements
Must have
• A professional and nautical look.
Nice to have
• May be nice to have a muted chart as the background design
Should not have
• colors or design that obscure the message of offering a wide range of professional boat captain services

```html
<!DOCTYPE html>
<html lang="en">
<head>
<meta charset="utf-8">
<title>Bluewake Harbor Skipper Services LLC – Business Card</title>
<link rel="stylesheet" href="https://fonts.googleapis.com/css2?family=Montserrat:wght@400;500;700;800&display=swap">
<style>
  :root {
    --page-bg: #eef0f3;
    --chart-deep: #aebdd1;
    --chart-light: #dfe6ef;
    --panel: #ffffff;
    --ink: #3d4a66;
    --ink-soft: #4c5874;
    --accent: #5aaee2;
  }
  * { box-sizing: border-box; margin: 0; padding: 0; }
  html, body {
    width: 1200px; height: 900px; overflow: hidden;
    background: var(--page-bg);
    font-family: "Montserrat", sans-serif;
    color: var(--ink);
  }
  .business-card {
    position: absolute; left: 75px; top: 150px;
    width: 1050px; height: 600px;
    overflow: hidden;
    box-shadow: 0 18px 40px rgba(40, 55, 80, 0.18);
  }
  .chart-background {
    position: absolute; inset: 0;
    background:
      radial-gradient(ellipse at 70% 35%, var(--chart-light) 0%, transparent 55%),
      radial-gradient(ellipse at 20% 75%, #d3dce8 0%, transparent 50%),
      linear-gradient(135deg, #c3cfdd 0%, var(--chart-deep) 100%);
  }
  .panel { position: absolute; background: var(--panel); }

  .brand-panel {
    left: 50px; top: 205px; width: 510px; height: 310px;
    display: flex; flex-direction: column; align-items: center; justify-content: center;
    text-align: center; padding: 0 40px;
  }
  .brand-mark {
    width: 48px; height: 48px; border-radius: 50%;
    background: var(--accent); margin-bottom: 20px;
  }
  .brand-name {
    font-weight: 800; font-size: 30px; line-height: 1.15;
    color: var(--ink); letter-spacing: -0.3px;
  }
  .services {
    margin-top: 22px; font-size: 19px; font-weight: 500;
    line-height: 1.35; color: var(--ink-soft);
  }

  .captain-panel {
    left: 650px; top: 40px; width: 350px; height: 115px;
    padding: 18px 26px; font-size: 21px; line-height: 1.25;
  }
  .captain-name { font-weight: 700; }
  .credential { font-weight: 500; }

  .contact-panel {
    left: 590px; top: 330px; width: 430px; height: 160px;
    padding: 22px 26px; text-align: right;
    font-size: 19px; font-weight: 500; line-height: 1.35;
    font-style: normal;
  }
  .contact-panel .email { display: block; margin-top: 12px; font-size: 17px; }
</style>
</head>
<body>
  <article class="business-card">
    <div class="chart-background" role="img" aria-label="Muted nautical world chart with grid lines and ocean labels"></div>

    <section class="panel brand-panel">
      <div class="brand-mark"></div>
      <h1 class="brand-name">Bluewake Harbor Skipper Services LLC</h1>
      <p class="services">Motor and Sailing Vessel Delivery, Charter, Surveys, Towing and Instruction</p>
    </section>

    <section class="panel captain-panel">
      <p class="captain-name">Captain Dale Murrow</p>
      <p class="credential">USCG Master Mariner</p>
      <p class="credential">200 ton, Ocean</p>
    </section>

    <address class="panel contact-panel">
      48215 Willowmere Lane<br>
      Fairfax Station, VA 22871<br>
      (C) 703-555-0187
      <span class="email">BluewakeHarborSkipper@mailbay-example.com</span>
    </address>
  </article>
</body>
</html>
```